Gumleaf Climate Crew WA Truck

I want a truck desing that screams Professional, Friendly and serious about work. you can find some of our work on our website, facebook and instagram.
https://breezelinecrew.example.com.au/
https://www.instagram.com/bzcrewox/
https://www.facebook.com/profile.php?id=70318825094631

The design needs to include our refrigeration license: AU38452 and electrical License: EC94031
I want the colours to be consistent with my Logo.

Key Notes to be included in the design, I want to let people know we do the following;
- Commercial and Residential
- Repairs, Service and Installation
- Reverse cycle ducted Air Conditioning
- Wall Split Air Conditioning
- Ceiling Cassettes
- Evaporative Air Conditioning
- Cool Rooms
- Display Fridges
- Beer Chillers

```html
<!DOCTYPE html>
<html lang="en">
<head>
<meta charset="utf-8">
<title>Gumleaf Climate Crew WA – Truck Side Panels</title>
<link rel="stylesheet" href="https://fonts.googleapis.com/css2?family=Oswald:wght@500;700&family=Montserrat:wght@700&display=swap">
<style>
  :root {
    --orange-deep: #d9531e;
    --orange-mid: #ee7a1c;
    --orange-light: #f6a21e;
    --amber: #f2b23a;
    --navy: #173a73;
    --blue: #1d77c2;
    --blue-light: #2f97dc;
    --white: #ffffff;
    --backdrop: #eef1f5;
  }
  * { margin: 0; padding: 0; box-sizing: border-box; }
  html, body {
    width: 1200px; height: 1200px; overflow: hidden;
    background: var(--backdrop);
  }
  .sheet {
    width: 1200px; height: 1200px;
    display: flex; flex-direction: column; justify-content: center; align-items: center;
    gap: 40px;
  }
  .truck-panel {
    width: 1100px; height: 530px; display: block;
    box-shadow: 0 4px 18px rgba(0,0,0,.12);
  }
  .service-list { font-family: "Oswald", sans-serif; font-weight: 500; font-size: 8.6px; fill: var(--white); letter-spacing: .2px; }
  .phone { font-family: "Oswald", sans-serif; font-weight: 500; font-size: 20px; fill: var(--white); letter-spacing: .6px; }
  .web { font-family: "Montserrat", sans-serif; font-weight: 700; font-size: 8px; fill: var(--white); }
  .web-navy { font-family: "Montserrat", sans-serif; font-weight: 700; font-size: 10px; fill: var(--navy); }
  .licence { font-family: "Oswald", sans-serif; font-weight: 700; font-size: 8.5px; fill: var(--navy); }
  .licence-light { font-family: "Oswald", sans-serif; font-weight: 500; font-size: 13px; fill: var(--white); }
  .brand-name { font-family: "Oswald", sans-serif; font-weight: 700; font-size: 24px; fill: var(--orange-mid); letter-spacing: .5px; }
  .bullet { fill: var(--navy); }
  .social-dot { fill: none; stroke: var(--white); stroke-width: 1.2; }
</style>
</head>
<body>
<main class="sheet">

  <svg class="truck-panel" viewBox="0 0 540 260" role="group" aria-label="Truck box side, version A">
    <defs>
      <linearGradient id="orangeA" x1="0" y1="0" x2="1" y2="1">
        <stop offset="0" stop-color="var(--orange-light)"/>
        <stop offset="1" stop-color="var(--orange-deep)"/>
      </linearGradient>
      <linearGradient id="phoneBarA" x1="0" y1="0" x2="1" y2="0">
        <stop offset="0" stop-color="var(--navy)"/>
        <stop offset=".7" stop-color="var(--blue)"/>
        <stop offset="1" stop-color="var(--blue-light)"/>
      </linearGradient>
    </defs>
    <rect class="box-white" width="540" height="260" fill="var(--white)"/>
    <path class="orange-block" d="M0 0 H225 C195 60 190 150 215 260 H0 Z" fill="url(#orangeA)"/>
    <path class="blue-swoosh" d="M225 0 H240 C208 70 205 160 232 260 H217 C190 160 193 65 225 0 Z" fill="var(--blue)"/>
    <rect class="phone-bar" x="0" y="196" width="212" height="30" fill="url(#phoneBarA)"/>
    <rect class="web-strip" x="0" y="228" width="218" height="20" fill="var(--orange-deep)"/>

    <g class="service-list">
      <circle class="bullet" cx="30" cy="27" r="2"/><text x="35" y="30">COMMERCIAL AND RESIDENTIAL</text>
      <circle class="bullet" cx="30" cy="41" r="2"/><text x="35" y="44">REPAIRS, SERVICE AND</text>
      <text x="35" y="58">INSTALLATION</text>
      <circle class="bullet" cx="30" cy="70" r="2"/><text x="35" y="73">REVERSE CYCLE DUCTED AIR</text>
      <text x="35" y="87">CONDITIONING</text>
      <circle class="bullet" cx="30" cy="99" r="2"/><text x="35" y="102">WALL SPLIT AIR CONDITIONING</text>
      <circle class="bullet" cx="30" cy="114" r="2"/><text x="35" y="117">CEILING CASSETTES</text>
      <circle class="bullet" cx="30" cy="128" r="2"/><text x="35" y="131">EVAPORATIVE AIR CONDITIONING</text>
      <circle class="bullet" cx="30" cy="143" r="2"/><text x="35" y="146">COOL ROOMS</text>
      <circle class="bullet" cx="30" cy="157" r="2"/><text x="35" y="160">DISPLAY FRIDGES</text>
      <circle class="bullet" cx="30" cy="172" r="2"/><text x="35" y="175">BEER CHILLERS</text>
    </g>
    <circle class="social-dot" cx="150" cy="186" r="5"/>
    <circle class="social-dot" cx="172" cy="186" r="5"/>
    <text class="phone" x="15" y="219">(870) 555-0142</text>
    <text class="web" x="15" y="241">www.gumleafcrew.example.com.au</text>

    <text class="brand-name" x="383" y="150" text-anchor="middle">Gumleaf Climate Crew WA</text>

    <text class="licence" x="475" y="230">AU38452</text>
    <text class="licence" x="475" y="244">LIC# EC94031</text>
  </svg>

  <svg class="truck-panel" viewBox="0 0 540 260" role="group" aria-label="Truck box side, version B">
    <defs>
      <linearGradient id="orangeB" x1="0" y1="0" x2="1" y2="1">
        <stop offset="0" stop-color="var(--orange-light)"/>
        <stop offset="1" stop-color="var(--orange-deep)"/>
      </linearGradient>
      <linearGradient id="bottomBandB" x1="0" y1="0" x2="1" y2="0">
        <stop offset="0" stop-color="var(--orange-deep)"/>
        <stop offset=".55" stop-color="var(--orange-mid)"/>
        <stop offset="1" stop-color="var(--amber)"/>
      </linearGradient>
    </defs>
    <rect class="box-white" width="540" height="260" fill="var(--white)"/>
    <path class="orange-block" d="M0 0 H160 L190 170 C195 190 205 196 225 196 H0 Z" fill="url(#orangeB)"/>
    <path class="blue-swoosh" d="M160 0 H176 L206 160 C212 188 222 200 250 200 H540 V210 H240 C205 210 195 195 188 165 Z" fill="var(--blue)"/>
    <path class="navy-swoosh" d="M176 0 H185 L214 155 C220 183 230 192 255 192 H540 V198 H250 C222 198 212 186 206 160 Z" fill="var(--navy)"/>
    <rect class="phone-bar" x="0" y="196" width="240" height="28" fill="var(--navy)"/>
    <rect class="bottom-band" x="0" y="224" width="540" height="26" fill="url(#bottomBandB)"/>

    <g class="service-list">
      <circle class="bullet" cx="22" cy="25" r="2"/><text x="27" y="28">WALL SPLIT AIR CONDITIONING</text>
      <circle class="bullet" cx="22" cy="40" r="2"/><text x="27" y="43">CEILING CASSETTES</text>
      <circle class="bullet" cx="22" cy="55" r="2"/><text x="27" y="58">EVAPORATIVE AIR CONDITIONING</text>
      <circle class="bullet" cx="22" cy="70" r="2"/><text x="27" y="73">COOL ROOMS</text>
      <circle class="bullet" cx="22" cy="85" r="2"/><text x="27" y="88">DISPLAY FRIDGES</text>
      <circle class="bullet" cx="22" cy="100" r="2"/><text x="27" y="103">BEER CHILLERS</text>
      <circle class="bullet" cx="22" cy="115" r="2"/><text x="27" y="118">COMMERCIAL AND RESIDENTIAL</text>
      <circle class="bullet" cx="22" cy="130" r="2"/><text x="27" y="133">REPAIRS, SERVICE AND INSTALLATION</text>
      <circle class="bullet" cx="22" cy="145" r="2"/><text x="27" y="148">REVERSE CYCLE DUCTED AIR</text>
      <text x="27" y="162">CONDITIONING</text>
    </g>
    <text class="phone" x="12" y="218">(870) 555-0142</text>
    <text class="licence-light" x="12" y="242">AU38452 LIC# EC94031</text>
    <circle class="social-dot" cx="243" cy="237" r="6"/>
    <circle class="social-dot" cx="262" cy="237" r="6"/>
    <text class="web-navy" x="278" y="241">www.gumleafcrew.example.com.au</text>

    <text class="brand-name" x="385" y="120" text-anchor="middle">Gumleaf Climate Crew WA</text>
  </svg>

</main>
</body>
</html>
```